Online Psychology Practice needs business cards.

Online Psychology service needs business cards. Have own logo- please see uploaded. I have other file formats if you need (not sure one needed?)

Details for Business Card:
Helena Marchetti
Clinical Psychologist BPsych, BPsych (Hons), MPsych (Clin), MAPS
T: 0439627015 | F: 08 73615204
E: hello@brightwatertelehealthcounselling.com.au
W: brightwatertelehealthcounselling.com.au

Industry/Entity Type

Health

Contact Information for Business Card

Logo plus details above (couldn't write in this section)

```html
<!DOCTYPE html>
<html lang="en">
<head>
<meta charset="utf-8">
<title>Brightwater Telehealth Counselling – Business Card</title>
<link rel="stylesheet" href="https://fonts.googleapis.com/css2?family=Arimo:wght@400;700&display=swap">
<style>
  :root {
    --backdrop: #2b2b2b;
    --card-white: #ffffff;
    --navy: #1b5a82;
    --teal: #1a8aa6;
    --ink: #1c1c1c;
    --rule: #9fb3c2;
  }
  * { box-sizing: border-box; margin: 0; padding: 0; }
  html, body {
    width: 1200px; height: 1059px; overflow: hidden;
    background: var(--backdrop);
    font-family: "Arimo", Arial, sans-serif;
  }
  .canvas { position: relative; width: 1200px; height: 1059px; }

  .card {
    position: absolute;
    border-radius: 16px;
    overflow: hidden;
  }
  .card-front {
    left: 257px; top: 89px; width: 693px; height: 390px;
    background: var(--card-white);
  }
  .card-back {
    left: 254px; top: 547px; width: 693px; height: 393px;
    background: var(--navy);
  }

  /* Front: brand block */
  .brand-front {
    position: absolute; right: 30px; top: 80px;
    display: flex; align-items: center; gap: 10px;
    width: 210px; justify-content: flex-end;
  }
  .brand-dot {
    flex: none; width: 26px; height: 26px; border-radius: 50%;
    background: var(--teal);
  }
  .brand-name {
    font-weight: 700; color: var(--navy);
    font-size: 19px; line-height: 1.15; text-align: left;
  }

  /* Front: person */
  .person { position: absolute; left: 22px; top: 158px; }
  .person-name {
    font-size: 24px; font-weight: 700; color: var(--navy);
    letter-spacing: 0.2px;
  }
  .person-title {
    margin-top: 5px;
    font-size: 15.5px; line-height: 20px; color: var(--teal);
  }
  .divider {
    position: absolute; left: 22px; top: 240px; width: 640px; height: 1px;
    background: linear-gradient(90deg, var(--rule), rgba(159,179,194,0.15));
  }

  /* Front: contacts */
  .contacts { position: absolute; left: 22px; top: 252px; list-style: none; }
  .contacts li {
    display: flex; align-items: center; gap: 7px;
    height: 22.5px; font-size: 16px; color: var(--ink);
  }
  .contacts svg { width: 12px; height: 12px; flex: none; fill: var(--navy); }

  .front-band { position: absolute; left: 0; bottom: 0; width: 693px; height: 40px; }

  /* Back */
  .brand-back {
    position: absolute; left: 0; right: 0; top: 110px;
    display: flex; flex-direction: column; align-items: center; gap: 22px;
  }
  .brand-back .brand-dot { width: 64px; height: 64px; background: var(--card-white); }
  .brand-back .brand-name {
    color: var(--card-white); font-size: 32px; text-align: center; line-height: 1.2;
  }
</style>
</head>
<body>
<div class="canvas">

  <section class="card card-front" aria-label="Business card front">
    <div class="brand-front">
      <span class="brand-dot"></span>
      <span class="brand-name">Brightwater<br>Telehealth<br>Counselling</span>
    </div>

    <div class="person">
      <h1 class="person-name">HELENA MARCHETTI</h1>
      <p class="person-title">Clinical Psychologist BPsych,<br>BPsych (Hons), MPsych (Clin), MAPS</p>
    </div>

    <div class="divider"></div>

    <ul class="contacts">
      <li>
        <svg viewBox="0 0 24 24" aria-hidden="true"><path d="M6.6 10.8a15.1 15.1 0 0 0 6.6 6.6l2.2-2.2c.3-.3.7-.4 1-.2 1.1.4 2.3.6 3.6.6.6 0 1 .4 1 1V20c0 .6-.4 1-1 1A17 17 0 0 1 3 4c0-.6.4-1 1-1h3.5c.6 0 1 .4 1 1 0 1.3.2 2.5.6 3.6.1.3 0 .7-.2 1z"/></svg>
        <span>0439627015</span>
      </li>
      <li>
        <svg viewBox="0 0 24 24" aria-hidden="true"><path d="M6 2h12v5H6zM3 8h18a2 2 0 0 1 2 2v7h-4v5H5v-5H1v-7a2 2 0 0 1 2-2zm4 7v5h10v-5z"/></svg>
        <span>08 73615204</span>
      </li>
      <li>
        <svg viewBox="0 0 24 24" aria-hidden="true"><path d="M2 5h20v14H2zm2 2v.4l8 5.3 8-5.3V7zm0 2.8V17h16V9.8l-8 5.3z"/></svg>
        <span>hello@brightwatertelehealthcounselling.com.au</span>
      </li>
      <li>
        <svg viewBox="0 0 24 24" aria-hidden="true"><path d="M12 2a10 10 0 1 0 0 20 10 10 0 0 0 0-20zm-1 17.9A8 8 0 0 1 4.2 10L9 14.8v1a2 2 0 0 0 2 2zm6.9-2.5A2 2 0 0 0 16 16h-1v-3a1 1 0 0 0-1-1H8v-2h2a1 1 0 0 0 1-1V7h2a2 2 0 0 0 2-2v-.4a8 8 0 0 1 2.9 12.8z"/></svg>
        <span>brightwatertelehealthcounselling.com.au</span>
      </li>
    </ul>

    <svg class="front-band" viewBox="0 0 693 40" preserveAspectRatio="none" aria-hidden="true">
      <rect x="0" y="13" width="352" height="5" fill="var(--teal)"/>
      <path d="M0 26 L338 26 C356 26 360 0 392 0 L693 0 L693 40 L0 40 Z" fill="var(--navy)"/>
    </svg>
  </section>

  <section class="card card-back" aria-label="Business card back">
    <div class="brand-back">
      <span class="brand-dot"></span>
      <span class="brand-name">Brightwater<br>Telehealth Counselling</span>
    </div>
  </section>

</div>
</body>
</html>
```